8 new icons - bootstrap feel (no 3d)

I am redesigning http://www.brightlatchworks.com with bootstrap (go figure).. ;-)
You can see a preview here:
brightlatchworks[dot]com/bs/index[dot]html
(sorry for the [dot]'s, I don't want this to get indexed by zennor)
I am looking for 8 new icons that will match the current color/design that I have already started. You can see the filler images to see where they will go.
- I would like them to be big enough for mobile
- No 3D
- Grab colors/style from new site
- Take a look at bootstrap's 3 icons here: http://plover.docknest.com/framelet/
- Icons should be flat or have a gradient like bootstraps above.
- The circuit board pattern is not needed for these icons.
If you don't know much about the printed circuit board industry, the first four (quick turn, prototype, production, ad multilayer) could be a little tricky, but, I believe after you read the descriptions and zennor them, you can come with some ideas.
Ideas:
- Quick turn, you could have "24 hours" in the middle with an arrow around them to represent the "turn around".
- Prototype PCBs are for low quantities, so you could have just one to five PCBs there.
- Production PCBs are for higher volumes, so having arrows going up or A LOT of PCBs would work.
- Multilayer PCBs are a multi layered printed circuit board, so having a board that shows the different layers would work great. You can zennor multialyer pcb and find some inspiration as well.
The other four (aerospace/military, medial/bio-medial, industrial/automotive, and students/hobbyist) seem to me to be really straight forward, so, I won't go into details about those. Be creative. :-)

```html
<!DOCTYPE html>
<html lang="en">
<head>
<meta charset="utf-8">
<title>Bright Latchworks – PCB Services</title>
<link href="https://fonts.googleapis.com/css2?family=Arimo:wght@400;700&display=swap" rel="stylesheet">
<style>
  :root {
    --page: #f2f2f2;
    --paper: #ffffff;
    --gold-light: #efe2b0;
    --gold-mid: #e2cf88;
    --gold-dark: #cfb868;
    --green: #2c5a2c;
    --green-dark: #1b3d1c;
    --olive: #8c8c10;
    --ink: #444444;
    --ink-soft: #555555;
    --nav-ink: #3d3a26;
    --rule: #dddddd;
    --card-border: #dedede;
  }
  * { box-sizing: border-box; margin: 0; padding: 0; }
  html, body { width: 1200px; height: 845px; overflow: hidden; }
  body { background: var(--page); font-family: "Arimo", Arial, sans-serif; color: var(--ink); position: relative; }
  .page { position: absolute; left: 0; top: 0; width: 1187px; height: 845px; background: var(--paper); }

  .hero { position: absolute; left: 32px; top: 0; width: 1137px; height: 245px;
    background: linear-gradient(180deg, var(--gold-dark) 0%, var(--gold-mid) 45%, var(--gold-light) 100%); }
  .anniversary { position: absolute; left: 53px; top: 12px; width: 290px; height: 150px;
    border-radius: 8px; background: linear-gradient(180deg, #2f5c2c, #1f4420); }
  .quote-cta { position: absolute; left: 768px; top: 44px; width: 380px; height: 91px;
    background: linear-gradient(180deg, #3d6e3a 0%, var(--green) 55%, var(--green-dark) 100%);
    border-radius: 3px; color: #fff; text-align: center; text-decoration: none; box-shadow: 0 3px 6px rgba(0,0,0,.35); }
  .quote-cta__title { display: block; font-weight: 700; font-size: 31px; margin-top: 13px; letter-spacing: .5px; text-shadow: 0 2px 2px rgba(0,0,0,.4); }
  .quote-cta__sub { display: block; font-size: 18px; margin-top: 1px; letter-spacing: .5px; }
  .quote-cta__fold { position: absolute; right: 0; bottom: -13px; width: 0; height: 0;
    border-top: 13px solid #142c14; border-right: 13px solid transparent; }

  .perks { position: absolute; left: 0; width: 1137px; text-align: center; font-size: 18.5px; color: var(--nav-ink); white-space: nowrap; }
  .perks--one { top: 180px; }
  .perks--two { top: 206px; }
  .perks span { margin: 0 4px; }
  .perks .sep { color: #5a5640; }
  .perks svg { width: 15px; height: 15px; vertical-align: -1px; margin-right: 4px; fill: var(--nav-ink); }

  .section-title { position: absolute; top: 268px; font-size: 22.5px; font-weight: 700; color: var(--ink); }
  .section-title--services { left: 32px; }
  .section-title--reviews { left: 831px; }

  .service-card { position: absolute; top: 321px; width: 369px; height: 495px; border: 1px solid var(--card-border); border-radius: 4px; background: #fff; }
  .service-card--quick { left: 32px; }
  .service-card--proto { left: 417px; }
  .service-card--next { top: 842px; height: 40px; }
  .service-card__art { position: absolute; }
  .service-card--quick .service-card__art { left: 61px; top: 1px; width: 250px; height: 250px; border-radius: 6px;
    background: linear-gradient(135deg, #2f4d08, var(--olive)); }
  .service-card--proto .service-card__art { left: 9px; top: 4px; width: 346px; height: 232px; border-radius: 10px;
    background: linear-gradient(135deg, #8a8a12 0%, #4f6a0c 55%, #153d06 100%); }
  .service-card__title { position: absolute; left: 17px; top: 261px; font-size: 18.5px; font-weight: 700; color: #333; }
  .service-card__text { position: absolute; left: 17px; top: 290px; font-size: 16.2px; line-height: 25px; color: var(--ink-soft); }
  .service-card--quick .service-card__text { width: 318px; }
  .service-card--proto .service-card__text { width: 326px; }

  .review { position: absolute; left: 832px; width: 330px; border-left: 5px solid var(--rule); padding-left: 19px; }
  .review--one { top: 321px; }
  .review--two { top: 593px; }
  .review__text { font-size: 15.5px; line-height: 25px; color: var(--ink-soft); width: 300px; }
  .review__by { margin-top: 8px; font-size: 13px; font-weight: 700; color: #888; display: flex; align-items: center; gap: 14px; }
  .review__mark { font-size: 17px; font-weight: 700; color: #777; }
  .review-divider { position: absolute; left: 832px; width: 338px; border-top: 1px dashed #d4d4d4; }
</style>
</head>
<body>
<div class="page">
  <header class="hero">
    <div class="anniversary" role="img" aria-label="Anniversary emblem: celebrating 30 years, 1982 to 2012"></div>

    <a class="quote-cta" href="#quote">
      <span class="quote-cta__title">Quote Request</span>
      <span class="quote-cta__sub">free, fast, and secure.</span>
      <span class="quote-cta__fold"></span>
    </a>

    <p class="perks perks--one">
      <span><svg viewBox="0 0 16 16"><rect x="1" y="3" width="14" height="10" fill="none" stroke="#3d3a26" stroke-width="2"/><circle cx="8" cy="8" r="2.5"/></svg>Manufacture Direct Pricing</span><span class="sep">|</span>
      <span><svg viewBox="0 0 16 16"><circle cx="8" cy="8" r="7"/></svg>Corporate Values</span><span class="sep">|</span>
      <span><svg viewBox="0 0 16 16"><path d="M1 4h4l6 8h4M1 12h4l6-8h4" fill="none" stroke="#3d3a26" stroke-width="2"/></svg>Diverse Capabilities</span><span class="sep">|</span>
      <span><svg viewBox="0 0 16 16"><path d="M9 0 3 9h4l-1 7 6-9H8z"/></svg>Fast Turnarounds</span>
    </p>
    <p class="perks perks--two">
      <span><svg viewBox="0 0 16 16"><path d="M3 1h10v5a5 5 0 0 1-10 0zM6 12h4v2H6z"/></svg>Quality Customer Service</span><span class="sep">|</span>
      <span><svg viewBox="0 0 16 16"><path d="M8 15 1 7a4 4 0 0 1 7-4 4 4 0 0 1 7 4z"/></svg>Trusted Experience</span><span class="sep">|</span>
      <span><svg viewBox="0 0 16 16"><rect x="1" y="1" width="14" height="14" fill="none" stroke="#3d3a26" stroke-width="2"/><rect x="4" y="8" width="2" height="5"/><rect x="7" y="5" width="2" height="8"/><rect x="10" y="9" width="2" height="4"/></svg>Low Minimums</span><span class="sep">|</span>
      <span><svg viewBox="0 0 16 16"><path d="M1 7h3v8H1zM5 7l4-6c2 0 2 2 1 5h5v4l-2 5H5z"/></svg>Guaranteed Quality</span>
    </p>
  </header>

  <h2 class="section-title section-title--services">PCB Services</h2>

  <article class="service-card service-card--quick">
    <div class="service-card__art" role="img" aria-label="Icon: the number 24 inside a circular turnaround arrow"></div>
    <h3 class="service-card__title">Quick turn, Fast, and Rapid PCBs.</h3>
    <p class="service-card__text">We specialize in Quick turn PCB services with and industry leading turnaround time as fast as 24 hours. When your organization needs fast and rapid PCB prototyping, know that you can count on Bright Latchworks to deliver high quality printed circuit boards on time.</p>
  </article>

  <article class="service-card service-card--proto">
    <div class="service-card__art" role="img" aria-label="Icon: a single printed circuit board with traces and pads"></div>
    <h3 class="service-card__title">Prototype PCBs.</h3>
    <p class="service-card__text">Perfect for testing or one-offs, utilize our entry-level prototype PCB services with up to 500 boards completed in a few days. With extensive prototype PCB fabrication capabilities, we are confident that will be able to exceed your organization's prototype requirements.</p>
  </article>

  <div class="service-card service-card--next" style="left:32px"></div>
  <div class="service-card service-card--next" style="left:417px"></div>

  <h2 class="section-title section-title--reviews">Testimonials / Reviews.</h2>

  <blockquote class="review review--one">
    <p class="review__text">I was impressed with the quality of the boards and the professionalism of Bright Latchworks' manufacturing department...You have exceeded your competitors in the quality of the product and the way in which the service was delivered.</p>
    <p class="review__by">— Marcus L. <span class="review__mark">Kestrel</span></p>
  </blockquote>

  <div class="review-divider" style="top:572px"></div>

  <blockquote class="review review--two">
    <p class="review__text">I just wanted to drop you a line and say thanks for your service Bright Latchworks! Everything turned out great, the boards worked fine on the first prototype, and your service was just what we had hoped for. Quality work in an excellent timeframe.</p>
    <p class="review__by">— Owen R. <span class="review__mark">Loftgrid</span></p>
  </blockquote>

  <div class="review-divider" style="top:843px"></div>
</div>
</body>
</html>
```